How do I determine which religion is correct?

This Infographic is part of the series "The Copper Lantern" found on my website www.brightmeadowpath.org.
This flow chart demonstrates a logical progression to determine which religion is correct based on historical factors and communication from the greatest conceivable being or God.

The main part of the sheet is the thought process starting with the question "How to I determine which religion is correct?"
The first question "Is the religion extant?" That is does the religion still exist. To the left you see no, these are defunct religions. To the right yes are religions that still exist and so pass on through the next question.

There are 5 main questions. The religions that get a no go into the "discarded bin" and the yes pass into the next question. Kind of like a funnel. Until the the end
The last question "Is there one eternal creator being?" Should be "Does the religion teach one eternal greatest conceivable being?" Also Hinduism should go to the "Yes" side not the no.

The 5 questions with the triangle have corresponding articles on the website. Also the right most questions in the flag-like box also have articles on the website and are associated with the question to the left. These articles and question provide more information.

This infographic is a quick reference to understand the thought process. I kind of like the idea of a funnel and waste basket, but I don't want to limit your creativity. I really like what you did on my last project, your design was beyond my best hopes.

If somehow these questions could be clickable links to the website that would be amazing.

```html
<!DOCTYPE html>
<html lang="en">
<head>
<meta charset="utf-8">
<title>How do I determine which religion is correct?</title>
<link href="https://fonts.googleapis.com/css2?family=Barlow:wght@400;500;600;700&family=Barlow+Semi+Condensed:wght@700&display=swap" rel="stylesheet">
<style>
  :root{
    --teal:#10b4b6;
    --teal-dark:#0a8788;
    --teal-deep:#077576;
    --teal-box:#0f9ea0;
    --teal-soft:#8fd9da;
    --mist:#dff0ef;
    --green:#119d4b;
    --green-edge:#5cc489;
    --red:#e9202b;
    --red-text:#b8252a;
    --rust:#c0714f;
    --white:#ffffff;
  }
  html,body{margin:0;padding:0;overflow:hidden;background:var(--white)}
  .canvas{position:relative;width:1200px;height:777px;overflow:hidden;font-family:"Barlow",sans-serif}
  .canvas svg{position:absolute;left:0;top:0}
  .title{font-family:"Barlow Semi Condensed",sans-serif;font-weight:700;font-size:37px;fill:var(--teal);text-anchor:middle}
  .series-head{font-family:"Barlow",sans-serif;font-weight:700;font-size:15px;fill:var(--white)}
  .brand{font-family:"Barlow",sans-serif;font-weight:500;font-size:22px;fill:var(--white)}
  .question{font-family:"Barlow",sans-serif;font-weight:600;font-size:14px;fill:var(--white);text-anchor:middle}
  .question-link:hover .question{fill:#fff6c8}
  .next{font-family:"Barlow",sans-serif;font-weight:600;font-size:11px;fill:var(--teal-deep);text-anchor:middle}
  .badge{font-family:"Barlow",sans-serif;font-weight:600;font-size:11px;fill:var(--white);text-anchor:middle}
  .list{font-family:"Barlow",sans-serif;font-size:10.5px;fill:var(--white);text-anchor:middle}
  .article{font-family:"Barlow",sans-serif;font-size:10px;fill:var(--white);text-anchor:middle}
  .article-link:hover rect{fill:var(--teal-dark)}
  .bin-text{font-family:"Barlow",sans-serif;font-size:12.5px;fill:var(--red-text);text-anchor:middle}
  .footer{font-family:"Barlow",sans-serif;font-size:15px;fill:var(--teal)}
</style>
</head>
<body>
<div class="canvas">
<svg width="1200" height="777" viewBox="0 0 1200 777" xmlns="http://www.w3.org/2000/svg">
  <defs>
    <linearGradient id="next-fade" x1="0" y1="0" x2="0" y2="1">
      <stop offset="0" stop-color="#0a8788"/>
      <stop offset="1" stop-color="#e6f3f3"/>
    </linearGradient>
    <linearGradient id="band-fade" x1="0" y1="0" x2="1" y2="0">
      <stop offset="0" stop-color="#e3f1ee" stop-opacity="0"/>
      <stop offset="0.12" stop-color="#e3f1ee"/>
      <stop offset="1" stop-color="#e3f1ee"/>
    </linearGradient>
    <linearGradient id="photo-tone" x1="0" y1="0" x2="1" y2="1">
      <stop offset="0" stop-color="#7a4a2e"/>
      <stop offset="0.5" stop-color="#e9e2d6"/>
      <stop offset="1" stop-color="#5a3524"/>
    </linearGradient>
    <linearGradient id="bin-tone" x1="0" y1="0" x2="0" y2="1">
      <stop offset="0" stop-color="#f6b8a0"/>
      <stop offset="1" stop-color="#f19a84"/>
    </linearGradient>
  </defs>

  <!-- header -->
  <rect class="header-band" x="0" y="0" width="1200" height="167" fill="var(--teal)"/>
  <rect class="series-band" x="701" y="80" width="499" height="87" fill="var(--teal-dark)"/>
  <path class="title-panel" d="M235,0 H701 V140 Q701,150 694,157 L664,188 H274 L243,157 Q235,150 235,140 Z" fill="var(--mist)"/>

  <g class="brand-mark">
    <circle cx="46" cy="55" r="12" fill="var(--white)"/>
    <text class="brand" x="66" y="63">Lanternwise</text>
  </g>

  <text class="title" x="470" y="74">HOW DO I DETERMINE</text>
  <text class="title" x="470" y="112">WHICH RELIGION IS</text>
  <text class="title" x="470" y="150">CORRECT?</text>

  <text class="series-head" x="872" y="133">THE COPPER LANTERN</text>
  <text class="series-head" x="872" y="152">SERIES</text>
  <text class="series-head" x="1050" y="112">WHAT IS THE</text>
  <text class="series-head" x="1050" y="131">PURPOSE OF</text>
  <text class="series-head" x="1050" y="150">COMMUNICATION?</text>

  <!-- discard bin area -->
  <g class="discard-bin">
    <rect x="26" y="122" width="199" height="589" rx="10" fill="url(#bin-tone)" role="img" aria-label="Illustration of a red wheeled waste bin holding the discarded religions"/>
    <text class="bin-text" x="126" y="216">Greek</text>
    <text class="bin-text" x="126" y="231">Roman</text>
    <text class="bin-text" x="126" y="246">etc</text>
    <text class="bin-text" x="126" y="311">Islam</text>
    <text class="bin-text" x="126" y="326">Christianity</text>
    <text class="bin-text" x="126" y="341">Sikhism</text>
    <text class="bin-text" x="126" y="407">Chinese/ African</text>
    <text class="bin-text" x="126" y="422">Tradition</text>
    <text class="bin-text" x="126" y="437">Ethnic</text>
    <text class="bin-text" x="126" y="509">Buddhism</text>
    <text class="bin-text" x="126" y="524">Zoroastrianism</text>
    <text class="bin-text" x="126" y="612">Jainism</text>
    <line x1="6" y1="713" x2="244" y2="713" stroke="#9a9a9a" stroke-width="1"/>
  </g>

  <!-- right side rows -->
  <g class="row-bands">
    <rect x="648" y="181" width="521" height="90" rx="22" fill="url(#band-fade)"/>
    <rect x="640" y="276" width="529" height="90" rx="22" fill="url(#band-fade)"/>
    <rect x="620" y="372" width="549" height="90" rx="22" fill="url(#band-fade)"/>
    <rect x="600" y="467" width="569" height="90" rx="22" fill="url(#band-fade)"/>
    <rect x="580" y="562" width="589" height="90" rx="22" fill="url(#band-fade)"/>
  </g>

  <!-- funnel -->
  <g class="funnel">
    <polygon points="274,194 661,194 648,259 287,259" fill="var(--teal)"/>
    <polygon points="294,289 641,289 628,354 307,354" fill="var(--teal)"/>
    <polygon points="315,385 620,385 607,450 328,450" fill="var(--teal)"/>
    <polygon points="335,480 600,480 587,545 348,545" fill="var(--teal)"/>
    <polygon points="355,575 580,575 567,640 368,640" fill="var(--teal)"/>

    <polygon points="287,259 648,259 641,289 294,289" fill="var(--teal-deep)"/>
    <polygon points="307,354 628,354 620,385 315,385" fill="var(--teal-deep)"/>
    <polygon points="328,450 607,450 600,480 335,480" fill="var(--teal-deep)"/>
    <polygon points="348,545 587,545 580,575 355,575" fill="var(--teal-deep)"/>
    <polygon points="368,640 567,640 560,670 376,670" fill="var(--teal-deep)"/>
    <polygon points="376,670 560,670 467,734" fill="var(--teal)"/>
    <rect class="agreement-icon" x="445" y="672" width="44" height="32" rx="6" fill="var(--teal-soft)" role="img" aria-label="Handshake icon marking agreement at the end of the funnel"/>

    <g class="next-step">
      <rect x="430" y="243" width="75" height="20" fill="url(#next-fade)"/>
      <polygon points="408,263 526,263 467,296" fill="#e6f3f3"/>
      <text class="next" x="467" y="278">NEXT</text>
      <rect x="430" y="338" width="75" height="20" fill="url(#next-fade)"/>
      <polygon points="408,358 526,358 467,391" fill="#e6f3f3"/>
      <text class="next" x="467" y="377">NEXT</text>
      <rect x="430" y="434" width="75" height="20" fill="url(#next-fade)"/>
      <polygon points="408,454 526,454 467,487" fill="#e6f3f3"/>
      <text class="next" x="467" y="472">NEXT</text>
      <rect x="430" y="529" width="75" height="20" fill="url(#next-fade)"/>
      <polygon points="408,549 526,549 467,582" fill="#e6f3f3"/>
      <text class="next" x="467" y="567">NEXT</text>
    </g>

    <a class="question-link" href="https://www.brightmeadowpath.org/is-the-religion-extant">
      <text class="question" x="467" y="226">Is the religion extant?</text></a>
    <a class="question-link" href="https://www.brightmeadowpath.org/is-the-religion-old">
      <text class="question" x="467" y="322">Is the religion old?</text></a>
    <a class="question-link" href="https://www.brightmeadowpath.org/is-there-a-written-tradition">
      <text class="question" x="467" y="414">Is there a written Tradition?</text></a>
    <a class="question-link" href="https://www.brightmeadowpath.org/more-than-one-communication">
      <text class="question" x="467" y="505">Does religion claim &gt;1</text>
      <text class="question" x="467" y="520">communication?</text></a>
    <a class="question-link" href="https://www.brightmeadowpath.org/one-eternal-greatest-being">
      <text class="question" x="467" y="598">Does the religion teach</text>
      <text class="question" x="467" y="612">one eternal greatest</text>
      <text class="question" x="467" y="627">conceivable being?</text></a>
  </g>

  <!-- NO branches -->
  <g class="no-branch">
    <line x1="280" y1="227" x2="222" y2="227" stroke="var(--rust)" stroke-width="2"/>
    <line x1="300" y1="322" x2="222" y2="322" stroke="var(--rust)" stroke-width="2"/>
    <line x1="321" y1="418" x2="222" y2="418" stroke="var(--rust)" stroke-width="2"/>
    <line x1="341" y1="513" x2="222" y2="513" stroke="var(--rust)" stroke-width="2"/>
    <line x1="361" y1="608" x2="222" y2="608" stroke="var(--rust)" stroke-width="2"/>
    <polygon points="216,227 229,221 229,233" fill="var(--red)"/>
    <polygon points="216,322 229,316 229,328" fill="var(--red)"/>
    <polygon points="216,418 229,412 229,424" fill="var(--red)"/>
    <polygon points="216,513 229,507 229,519" fill="var(--red)"/>
    <polygon points="216,608 229,602 229,614" fill="var(--red)"/>
    <circle cx="257" cy="227" r="15.5" fill="var(--red)"/>
    <circle cx="257" cy="322" r="15.5" fill="var(--red)"/>
    <circle cx="257" cy="418" r="15.5" fill="var(--red)"/>
    <circle cx="257" cy="513" r="15.5" fill="var(--red)"/>
    <circle cx="257" cy="608" r="15.5" fill="var(--red)"/>
    <text class="badge" x="257" y="231">NO</text>
    <text class="badge" x="257" y="326">NO</text>
    <text class="badge" x="257" y="422">NO</text>
    <text class="badge" x="257" y="517">NO</text>
    <text class="badge" x="257" y="612">NO</text>
  </g>

  <!-- YES branches -->
  <g class="yes-branch">
    <line x1="655" y1="227" x2="714" y2="227" stroke="var(--green)" stroke-width="2"/>
    <line x1="636" y1="322" x2="714" y2="322" stroke="var(--green)" stroke-width="2"/>
    <line x1="614" y1="418" x2="714" y2="418" stroke="var(--green)" stroke-width="2"/>
    <line x1="594" y1="513" x2="714" y2="513" stroke="var(--green)" stroke-width="2"/>
    <line x1="574" y1="608" x2="714" y2="608" stroke="var(--green)" stroke-width="2"/>
    <polygon points="720,227 707,221 707,233" fill="var(--green)"/>
    <polygon points="720,322 707,316 707,328" fill="var(--green)"/>
    <polygon points="720,418 707,412 707,424" fill="var(--green)"/>
    <polygon points="720,513 707,507 707,519" fill="var(--green)"/>
    <polygon points="720,608 707,602 707,614" fill="var(--green)"/>
    <circle cx="680" cy="227" r="15.5" fill="var(--green)"/>
    <circle cx="680" cy="322" r="15.5" fill="var(--green)"/>
    <circle cx="680" cy="418" r="15.5" fill="var(--green)"/>
    <circle cx="680" cy="513" r="15.5" fill="var(--green)"/>
    <circle cx="680" cy="608" r="15.5" fill="var(--green)"/>
    <text class="badge" x="680" y="231">YES</text>
    <text class="badge" x="680" y="326">YES</text>
    <text class="badge" x="680" y="422">YES</text>
    <text class="badge" x="680" y="517">YES</text>
    <text class="badge" x="680" y="612">YES</text>
  </g>

  <!-- passing religions -->
  <g class="pass-list">
    <line x1="844" y1="227" x2="894" y2="227" stroke="var(--green)" stroke-width="2"/>
    <line x1="844" y1="322" x2="894" y2="322" stroke="var(--green)" stroke-width="2"/>
    <circle cx="894" cy="227" r="5.5" fill="var(--white)" stroke="var(--green)" stroke-width="1.5"/>
    <circle cx="894" cy="322" r="5.5" fill="var(--white)" stroke="var(--green)" stroke-width="1.5"/>

    <rect x="727" y="188" width="117" height="78" rx="9" fill="var(--green)" stroke="var(--green-edge)" stroke-width="1.5"/>
    <text class="list" x="785" y="204">Christianity</text>
    <text class="list" x="785" y="217.5">Islam</text>
    <text class="list" x="785" y="231">Hinduism</text>
    <text class="list" x="785" y="244.5">Buddhism</text>
    <text class="list" x="785" y="258">Judaism</text>

    <rect x="894" y="188" width="117" height="78" rx="9" fill="var(--green)" stroke="var(--green-edge)" stroke-width="1.5"/>
    <text class="list" x="952" y="204">Chinese Tradition,</text>
    <text class="list" x="952" y="217.5">African Tradition,</text>
    <text class="list" x="952" y="231">Ethnic Religions,</text>
    <text class="list" x="952" y="244.5">Sikhism, Jainism,</text>
    <text class="list" x="952" y="258">Zoroastrianism</text>

    <rect x="727" y="283" width="117" height="78" rx="9" fill="var(--green)" stroke="var(--green-edge)" stroke-width="1.5"/>
    <text class="list" x="785" y="305">Hinduism</text>
    <text class="list" x="785" y="318.5">Buddhism</text>
    <text class="list" x="785" y="332">Judaism</text>
    <text class="list" x="785" y="345.5">Jainism</text>

    <rect x="894" y="283" width="117" height="78" rx="9" fill="var(--green)" stroke="var(--green-edge)" stroke-width="1.5"/>
    <text class="list" x="952" y="305">Chinese Tradition,</text>
    <text class="list" x="952" y="318.5">African Tradition,</text>
    <text class="list" x="952" y="332">Ethnic Religions,</text>
    <text class="list" x="952" y="345.5">Zoroastrianism</text>

    <rect x="727" y="378" width="117" height="78" rx="9" fill="var(--green)" stroke="var(--green-edge)" stroke-width="1.5"/>
    <text class="list" x="785" y="394">Hinduism</text>
    <text class="list" x="785" y="407.5">Buddhism</text>
    <text class="list" x="785" y="421">Judaism</text>
    <text class="list" x="785" y="434.5">Jainism</text>
    <text class="list" x="785" y="448">Zoroastrianism</text>

    <rect x="727" y="473" width="117" height="78" rx="9" fill="var(--green)" stroke="var(--green-edge)" stroke-width="1.5"/>
    <text class="list" x="785" y="502">Hinduism</text>
    <text class="list" x="785" y="515.5">Judaism</text>
    <text class="list" x="785" y="529">Jainism</text>

    <rect x="727" y="569" width="117" height="78" rx="9" fill="var(--green)" stroke="var(--green-edge)" stroke-width="1.5"/>
    <text class="list" x="785" y="604">Hinduism</text>
    <text class="list" x="785" y="617.5">Judaism</text>
  </g>

  <rect class="scripture-photo" x="868" y="390" width="170" height="145" rx="9" fill="url(#photo-tone)" role="img" aria-label="Photo of an open book with prayer beads resting on its pages"/>

  <!-- article flags -->
  <g class="articles">
    <a class="article-link" href="https://www.brightmeadowpath.org/why-must-the-religion-still-exist">
      <rect x="1063" y="188" width="99" height="78" rx="9" fill="var(--teal-box)"/>
      <text class="article" x="1112" y="224">Why must the</text>
      <text class="article" x="1112" y="237">religion still exist?</text></a>
    <a class="article-link" href="https://www.brightmeadowpath.org/why-must-the-religion-be-old">
      <rect x="1063" y="283" width="99" height="78" rx="9" fill="var(--teal-box)"/>
      <text class="article" x="1112" y="318">Why must the</text>
      <text class="article" x="1112" y="331">religion be old?</text></a>
    <a class="article-link" href="https://www.brightmeadowpath.org/why-written-tradition-matters">
      <rect x="1063" y="378" width="99" height="78" rx="9" fill="var(--teal-box)"/>
      <text class="article" x="1112" y="407">Why is a written</text>
      <text class="article" x="1112" y="420">tradition</text>
      <text class="article" x="1112" y="433">important?</text></a>
    <a class="article-link" href="https://www.brightmeadowpath.org/why-more-communications-matter">
      <rect x="1063" y="473" width="99" height="78" rx="9" fill="var(--teal-box)"/>
      <text class="article" x="1112" y="496">Why does 2 or</text>
      <text class="article" x="1112" y="509">more</text>
      <text class="article" x="1112" y="522">communications</text>
      <text class="article" x="1112" y="535">matter?</text></a>
    <a class="article-link" href="https://www.brightmeadowpath.org/why-a-first-cause">
      <rect x="850" y="569" width="100" height="78" rx="9" fill="var(--teal-box)"/>
      <text class="article" x="900" y="597">Why must</text>
      <text class="article" x="900" y="610">there be a first</text>
      <text class="article" x="900" y="623">cause?</text></a>
    <a class="article-link" href="https://www.brightmeadowpath.org/why-a-first-cause-part-two">
      <rect x="956" y="569" width="99" height="78" rx="9" fill="var(--teal-box)"/>
      <text class="article" x="1006" y="597">Why must</text>
      <text class="article" x="1006" y="610">there be a first</text>
      <text class="article" x="1006" y="623">cause?</text></a>
    <a class="article-link" href="https://www.brightmeadowpath.org/must-something-be-eternal">
      <rect x="1063" y="569" width="99" height="78" rx="9" fill="var(--teal-box)"/>
      <text class="article" x="1112" y="597">Does something</text>
      <text class="article" x="1112" y="610">have to be</text>
      <text class="article" x="1112" y="623">eternal?</text></a>
  </g>

  <!-- footer -->
  <text class="footer" x="30" y="732">© Copyright Bright Meadow Path</text>
  <text class="footer" x="1162" y="732" text-anchor="end">WWW.BRIGHTMEADOWPATH.ORG</text>
</svg>
</div>
</body>
</html>
```